Brantley Studios photography and video creator

I need a business card for my production company. I shoot photography and videography for real estate, adventure sports and businesses

Contact Information for Business Card

simple not to busy

Colors

Designer to choose colors to be used in the design.

Requirements
Must have
• derek@brantleystudios.ca
• phone -5873304127
• instagram derek_brantley

```html
<!DOCTYPE html>
<html lang="en">
<head>
<meta charset="utf-8">
<title>Brantley Studios – Business Card</title>
<link rel="stylesheet" href="https://fonts.googleapis.com/css2?family=Montserrat:wght@400;500;700&display=swap">
<style>
  :root {
    --bg: #d9d9d9;
    --card: #f4f4f4;
    --ink: #151515;
    --ink-soft: #3a3a3a;
    --sky-light: #ececec;
    --hill-mid: #8a8a8a;
    --hill-dark: #1c1c1c;
    --shadow: rgba(0, 0, 0, 0.18);
  }
  * { box-sizing: border-box; margin: 0; padding: 0; }
  html, body {
    width: 1200px;
    height: 1021px;
    overflow: hidden;
    background: var(--bg);
    font-family: "Montserrat", sans-serif;
    color: var(--ink);
  }
  .sheet {
    position: relative;
    width: 1200px;
    height: 1021px;
  }
  .card {
    position: absolute;
    left: 220px;
    width: 760px;
    height: 434px;
    background: var(--card);
    box-shadow: 0 6px 18px var(--shadow);
    overflow: hidden;
  }
  .card--front { top: 50px; }
  .card--back { top: 536px; }

  /* Front */
  .landscape {
    position: absolute;
    inset: 0;
    width: 100%;
    height: 100%;
  }
  .wordmark {
    position: absolute;
    top: 92px;
    right: 56px;
    text-align: right;
    font-weight: 700;
    color: var(--ink);
    line-height: 1;
  }
  .wordmark__name {
    display: block;
    font-size: 58px;
    letter-spacing: 1px;
  }
  .wordmark__sub {
    display: block;
    margin-top: 6px;
    font-size: 14px;
    letter-spacing: 9px;
  }

  /* Back */
  .emblem {
    position: absolute;
    left: 62px;
    top: 107px;
    width: 220px;
    height: 220px;
  }
  .emblem__label {
    position: absolute;
    left: 62px;
    top: 188px;
    width: 220px;
    text-align: center;
    color: #ffffff;
    font-weight: 700;
    line-height: 1;
  }
  .emblem__name {
    display: block;
    font-size: 30px;
    letter-spacing: 1px;
  }
  .emblem__sub {
    display: block;
    margin-top: 6px;
    font-size: 9px;
    letter-spacing: 5px;
  }
  .details {
    position: absolute;
    left: 370px;
    top: 128px;
  }
  .details__name {
    font-size: 23px;
    font-weight: 700;
    letter-spacing: 1px;
  }
  .details__role {
    font-size: 18px;
    font-weight: 500;
    color: var(--ink-soft);
    margin-top: 2px;
  }
  .details__rule {
    width: 44px;
    height: 3px;
    background: var(--ink);
    margin: 18px 0 20px;
  }
  .contact {
    list-style: none;
  }
  .contact__item {
    display: flex;
    align-items: center;
    gap: 8px;
    font-size: 19px;
    line-height: 28px;
  }
  .contact__icon {
    width: 17px;
    height: 17px;
    flex: none;
  }
</style>
</head>
<body>
<main class="sheet">

  <section class="card card--front" aria-label="Card front">
    <svg class="landscape" viewBox="0 0 760 434" preserveAspectRatio="none" role="img" aria-label="Monochrome mountain range with pine trees">
      <defs>
        <linearGradient id="hills" x1="0" y1="0" x2="0" y2="1">
          <stop offset="0" stop-color="var(--sky-light)"/>
          <stop offset="0.45" stop-color="#d2d2d2"/>
          <stop offset="0.7" stop-color="var(--hill-mid)"/>
          <stop offset="1" stop-color="var(--hill-dark)"/>
        </linearGradient>
      </defs>
      <rect width="760" height="434" fill="url(#hills)"/>
    </svg>
    <div class="wordmark">
      <span class="wordmark__name">BRANTLEY</span>
      <span class="wordmark__sub">STUDIOS</span>
    </div>
  </section>

  <section class="card card--back" aria-label="Card back">
    <svg class="emblem" viewBox="0 0 220 220" aria-hidden="true">
      <circle cx="110" cy="110" r="110" fill="var(--hill-dark)"/>
    </svg>
    <div class="emblem__label">
      <span class="emblem__name">BRANTLEY</span>
      <span class="emblem__sub">STUDIOS</span>
    </div>

    <div class="details">
      <h1 class="details__name">DEREK BRANTLEY</h1>
      <p class="details__role">Photographer</p>
      <div class="details__rule"></div>
      <ul class="contact">
        <li class="contact__item">
          <svg class="contact__icon" viewBox="0 0 24 24" aria-hidden="true">
            <path d="M6.6 10.8a15.1 15.1 0 0 0 6.6 6.6l2.2-2.2a1 1 0 0 1 1-.25 11.4 11.4 0 0 0 3.6.57 1 1 0 0 1 1 1V20a1 1 0 0 1-1 1A17 17 0 0 1 3 4a1 1 0 0 1 1-1h3.5a1 1 0 0 1 1 1c0 1.25.2 2.45.57 3.6a1 1 0 0 1-.25 1z" fill="var(--ink)"/>
          </svg>
          <span>587-330-4127</span>
        </li>
        <li class="contact__item">
          <svg class="contact__icon" viewBox="0 0 24 24" aria-hidden="true">
            <rect x="2" y="5" width="20" height="14" fill="none" stroke="var(--ink)" stroke-width="2"/>
            <path d="M2 5l10 8 10-8" fill="none" stroke="var(--ink)" stroke-width="2"/>
          </svg>
          <span>derek@brantleystudios.ca</span>
        </li>
        <li class="contact__item">
          <svg class="contact__icon" viewBox="0 0 24 24" aria-hidden="true">
            <circle cx="12" cy="12" r="9" fill="none" stroke="var(--ink)" stroke-width="2"/>
          </svg>
          <span>derek_brantley</span>
        </li>
      </ul>
    </div>
  </section>

</main>
</body>
</html>
```